Business cards Marta Keller Sport & Events

I need new business cards to match my new logo design for my company called "Marta Keller Sport & Events". I'm based in Germany.
With my company, I offer different services in the context of sport.

Marta Keller owner

Marta Keller Sports & Events
Birkendorfer Weg 14
D-63158 Offenbach

+49 69 / 31 52 94 07
info@marta-keller-sport.example
www.marta-keller-sport.example

Contact Information for Business Card

Marta Keller Inhaberin Marta Keller Sport & Events Birkendorfer Weg 14 D-63158 Offenbach +49 69 / 31 52 94 07 info@marta-keller-sport.example www.marta-keller-sport.example

Requirements
Must have
• Logo | Double sided business card

```html
<!DOCTYPE html>
<html lang="de">
<head>
<meta charset="utf-8">
<title>Marta Keller Sport &amp; Events – Visitenkarten</title>
<link href="https://fonts.googleapis.com/css2?family=Exo+2:wght@700&family=Montserrat:wght@400;600;700&display=swap" rel="stylesheet">
<style>
  :root {
    --orange: #f39c1f;
    --black: #1b1b1d;
    --white: #ffffff;
    --ink: #222222;
    --faint: #ececec;
    --stage: #e9e7e4;
  }
  * { box-sizing: border-box; margin: 0; padding: 0; }
  html, body { width: 1200px; height: 930px; overflow: hidden; }
  body {
    background: var(--stage);
    font-family: "Montserrat", Arial, sans-serif;
    color: var(--ink);
    position: relative;
  }
  .card {
    position: absolute;
    left: 300px;
    width: 600px;
    height: 390px;
    border-radius: 22px;
    overflow: hidden;
    box-shadow: 0 8px 24px rgba(0,0,0,0.18);
  }
  .card-back { top: 50px; background: var(--black); }
  .card-front { top: 490px; background: var(--white); }

  /* brand lockup: plain circle + name in one colour and weight */
  .brand {
    position: absolute;
    display: flex;
    align-items: center;
    gap: 18px;
  }
  .brand-dot {
    width: 78px; height: 78px;
    border-radius: 50%;
    background: var(--orange);
    flex: none;
  }
  .brand-name {
    font-weight: 700;
    font-size: 26px;
    letter-spacing: 2px;
    text-transform: uppercase;
    line-height: 1.15;
  }
  .card-back .brand { left: 0; right: 0; top: 150px; justify-content: center; }
  .card-back .brand-name { color: var(--white); }

  /* front */
  .front-band {
    position: absolute;
    left: 0; right: 0;
    top: 34px; height: 104px;
    background: var(--black);
  }
  .front-seal {
    position: absolute;
    left: 234px; top: 22px;
    width: 132px; height: 132px;
    border-radius: 50%;
    background: var(--white);
    display: flex; align-items: center; justify-content: center;
  }
  .front-seal .brand-dot { width: 110px; height: 110px; }
  .front-brand-name {
    position: absolute;
    left: 0; right: 0; top: 160px;
    text-align: center;
    font-weight: 700;
    font-size: 19px;
    letter-spacing: 2px;
    text-transform: uppercase;
    color: var(--ink);
  }
  .front-deco {
    position: absolute;
    left: 390px; top: 170px;
    width: 230px; height: 230px;
    border-radius: 50%;
    border: 26px solid var(--faint);
  }
  .person { position: absolute; left: 40px; top: 240px; }
  .person-name {
    font-family: "Exo 2", "Montserrat", sans-serif;
    font-weight: 700;
    font-size: 24px;
    color: var(--orange);
    text-transform: uppercase;
    line-height: 1;
  }
  .person-role { font-size: 17px; margin-top: 4px; }
  .contact-list { list-style: none; margin-top: 16px; }
  .contact-list li {
    display: flex; align-items: center; gap: 10px;
    font-size: 15px; line-height: 22px;
  }
  .contact-list svg { width: 13px; height: 13px; flex: none; }
  .address {
    position: absolute;
    right: 40px; top: 232px;
    text-align: right;
    font-size: 15px;
    line-height: 21px;
  }
  .address-company { color: var(--orange); }
</style>
</head>
<body>

<section class="card card-back" aria-label="Rückseite">
  <div class="brand">
    <span class="brand-dot"></span>
    <span class="brand-name">Marta Keller<br>Sport &amp; Events</span>
  </div>
</section>

<section class="card card-front" aria-label="Vorderseite">
  <div class="front-deco"></div>
  <div class="front-band"></div>
  <div class="front-seal"><span class="brand-dot"></span></div>
  <p class="front-brand-name">Marta Keller Sport &amp; Events</p>

  <div class="person">
    <p class="person-name">Marta Keller</p>
    <p class="person-role">owner</p>
    <ul class="contact-list">
      <li>
        <svg viewBox="0 0 16 16" fill="none" stroke="#f39c1f" stroke-width="1.8"><path d="M3 2l3 .5 1 3-2 1.5a8 8 0 0 0 4 4L10.5 9l3 1 .5 3-2 1.5C6 14 2 10 1.5 4z"/></svg>
        +49 69 / 31 52 94 07
      </li>
      <li>
        <svg viewBox="0 0 16 16" fill="none" stroke="#f39c1f" stroke-width="1.8"><rect x="1.5" y="3.5" width="13" height="9" rx="1"/><path d="M1.5 4l6.5 5 6.5-5"/></svg>
        info@marta-keller-sport.example
      </li>
      <li>
        <svg viewBox="0 0 16 16" fill="none" stroke="#f39c1f" stroke-width="1.5"><circle cx="8" cy="8" r="6.5"/><path d="M1.5 8h13M8 1.5c3 3.5 3 9.5 0 13M8 1.5c-3 3.5-3 9.5 0 13"/></svg>
        www.marta-keller-sport.example
      </li>
    </ul>
  </div>

  <address class="address" style="font-style: normal;">
    <span class="address-company">Marta Keller Sports &amp; Events</span><br>
    Birkendorfer Weg 14<br>
    D-63158 Offenbach
  </address>
</section>

</body>
</html>
```